Valbrina Soletti Winery 2023 Label

We are just about to bottle our very first Napa Valley Cabernet Sauvignon and need label ideas

Target Market(s)

Cab drinkers who like Napa California Cabs

Industry/Entity Type

Wine Making

Logo Text

Valbrina Soletti 2023 Napa Estate Grown Cabernet Sauvignon

Requirements
Must have
• Winery Name, year of vintage and Napa Estate Cab
Nice to have
• If using the initials V and S use gold letters on black or red background

```html
<!DOCTYPE html>
<html lang="en">
<head>
<meta charset="utf-8">
<title>Valbrina Soletti 2023 Napa Estate Grown Cabernet Sauvignon</title>
<link rel="stylesheet" href="https://fonts.googleapis.com/css2?family=Tinos:wght@700&display=swap">
<style>
  :root {
    --cream: #F7EFDF;
    --gold: #B5892A;
    --gold-light: #C9A14A;
    --gold-deep: #A57B22;
  }
  html, body {
    margin: 0;
    padding: 0;
    width: 871px;
    height: 1200px;
    overflow: hidden;
    background: var(--cream);
  }
  .label {
    position: relative;
    width: 871px;
    height: 1200px;
    background: var(--cream);
    color: var(--gold);
    font-family: "Tinos", "Times New Roman", serif;
    font-weight: 700;
  }
  .line {
    position: absolute;
    left: 0;
    width: 100%;
    margin: 0;
    text-align: center;
    line-height: 1;
    white-space: nowrap;
  }
  .winery-name { font-size: 148px; letter-spacing: -1px; }
  .winery-name--first { top: 111px; }
  .winery-name--second { top: 226px; }
  .crest {
    position: absolute;
    left: 183px;
    top: 388px;
    width: 505px;
    height: 273px;
  }
  .detail { font-size: 74px; }
  .vintage { top: 683px; }
  .region { top: 763px; }
  .estate { top: 842px; }
  .varietal-first { top: 922px; }
  .varietal-second { top: 1002px; }
</style>
</head>
<body>
  <main class="label">
    <h1 class="line winery-name winery-name--first">Valbrina</h1>
    <p class="line winery-name winery-name--second">Soletti</p>

    <svg class="crest" viewBox="0 0 505 273" role="img" aria-label="Heraldic crest illustration: two rampant lions supporting a shield with a banner beneath">
      <defs>
        <radialGradient id="crestTone" cx="50%" cy="50%" r="60%">
          <stop offset="0%" stop-color="var(--gold)" stop-opacity="0.55"/>
          <stop offset="100%" stop-color="var(--gold-light)" stop-opacity="0.2"/>
        </radialGradient>
      </defs>
      <rect x="0" y="0" width="505" height="273" rx="6" fill="url(#crestTone)"/>
    </svg>

    <p class="line detail vintage">2023</p>
    <p class="line detail region">NAPA</p>
    <p class="line detail estate">ESTATE GROWN</p>
    <p class="line detail varietal-first">CABERNET</p>
    <p class="line detail varietal-second">SAUVIGNON</p>
  </main>
</body>
</html>
```